Flyer für Partei
Zielgruppe
BVL = Bürgerliche Vernunft Liste Würzburg Stadt und Landkreis
BVL Fraktion Würzburg - Wir planen einen Neujahrsempfang und brauchen dafür eine Einladungskarte in DIN lang (für Kuvert lang passend)
Aufgabenstellung
Folgender Inhalt muss drauf sein
Einladung zum Neujahrsempfang am 31. Januar 2025
Titel: Können wir noch gemeinsam?
Populismus, Pauschalierung, Polarisierung – Demokratie in Krisenzeiten
Ablauf: 18.30 Uhr Ankommen
19.00 Uhr Begrüßung durch den Kreis- und Fraktionsvorsitzend
19.20 Uhr Festvortrag von Gernot Holzapf
20.00 Uhr Austausch
Veranstaltungsort: Lindmark Forum, Kastanienweg 7, 97080 Würzburg
Verantwortlich: T. Lohmeyer, Ahornring 4, 97082 Würzburg, tobias.lohmeyer@bvl-beispiel.de; Anmeldung erbeten

```html
<!DOCTYPE html>
<html lang="de">
<head>
<meta charset="utf-8">
<title>Einladung zum Neujahrsempfang – BVL Würzburg</title>
<link href="https://fonts.googleapis.com/css2?family=Source+Sans+3:wght@700&family=Roboto+Condensed:wght@400;700&display=swap" rel="stylesheet">
<style>
  :root {
    --purple: #8e1262;
    --purple-deep: #7d0f57;
    --orange: #f07800;
    --white: #ffffff;
    --sparkle: rgba(255, 255, 255, 0.55);
  }
  * { margin: 0; padding: 0; box-sizing: border-box; }
  html, body { width: 1200px; height: 600px; overflow: hidden; background: var(--purple); }
  .card {
    position: relative;
    width: 1200px;
    height: 600px;
    overflow: hidden;
    background: radial-gradient(ellipse at 60% 55%, var(--purple) 0%, var(--purple-deep) 100%);
    font-family: "Roboto Condensed", "Arial Narrow", sans-serif;
    font-weight: 700;
    color: var(--white);
  }
  .sparkles { position: absolute; inset: 0; }
  .headline {
    position: absolute;
    top: 18px;
    left: 0;
    width: 1200px;
    text-align: center;
    font-family: "Source Sans 3", Arial, sans-serif;
    font-size: 44px;
    letter-spacing: 0.2px;
  }
  .brand {
    position: absolute;
    left: 30px;
    top: 230px;
    font-size: 190px;
    line-height: 1;
    color: var(--orange);
  }
  .details {
    position: absolute;
    left: 34px;
    top: 458px;
    width: 360px;
    font-size: 16px;
    line-height: 21px;
    font-weight: 400;
  }
  .details strong { font-weight: 700; color: var(--orange); }
  .topic {
    position: absolute;
    left: 402px;
    top: 128px;
    font-size: 23px;
    line-height: 30px;
  }
  .schedule {
    position: absolute;
    left: 478px;
    top: 220px;
  }
  .schedule ul { list-style: none; }
  .schedule-label {
    display: inline-block;
    background: var(--orange);
    padding: 1px 6px;
    font-size: 24px;
    line-height: 30px;
    margin-bottom: 18px;
  }
  .schedule-item {
    font-size: 25px;
    line-height: 30px;
    height: 88px;
  }
  .schedule-item .time { color: var(--orange); }
</style>
</head>
<body>
  <main class="card">
    <svg class="sparkles" width="1200" height="600" aria-hidden="true">
      <defs>
        <radialGradient id="glow">
          <stop offset="0" stop-color="#fff" stop-opacity="0.8"/>
          <stop offset="1" stop-color="#fff" stop-opacity="0"/>
        </radialGradient>
      </defs>
      <circle cx="284" cy="104" r="7" fill="url(#glow)"/>
      <circle cx="556" cy="38" r="6" fill="url(#glow)"/>
      <circle cx="1090" cy="74" r="6" fill="url(#glow)"/>
      <circle cx="956" cy="256" r="8" fill="url(#glow)"/>
      <circle cx="1106" cy="400" r="7" fill="url(#glow)"/>
      <circle cx="760" cy="548" r="7" fill="url(#glow)"/>
      <circle cx="1000" cy="580" r="5" fill="url(#glow)"/>
      <circle cx="104" cy="424" r="6" fill="url(#glow)"/>
      <circle cx="432" cy="406" r="5" fill="url(#glow)"/>
    </svg>

    <h1 class="headline">Einladung zum Neujahrsempfang am 31. Januar 2025</h1>

    <div class="brand">BVL</div>

    <div class="details">
      <p><strong>Veranstaltungsort:</strong> Lindmark Forum,<br>Kastanienweg 7, 97080 Würzburg</p>
      <p><strong>Verantwortlich:</strong> T. Lohmeyer, Ahornring 4, 97082 Würzburg,<br>tobias.lohmeyer@bvl-beispiel.de</p>
      <p><strong>Anmeldung erbeten</strong></p>
    </div>

    <p class="topic">Können wir noch gemeinsam?<br>Populismus, Pauschalierung, Polarisierung – Demokratie in Krisenzeiten</p>

    <div class="schedule">
      <span class="schedule-label">Ablauf:</span>
      <ul>
        <li class="schedule-item"><span class="time">18.30 Uhr</span> Ankommen</li>
        <li class="schedule-item"><span class="time">19.00 Uhr</span> Begrüßung durch den Kreis- und Fraktionsvorsitzend</li>
        <li class="schedule-item"><span class="time">19.20 Uhr</span> Festvortrag von Gernot Holzapf</li>
        <li class="schedule-item"><span class="time">20.00 Uhr</span> Austausch</li>
      </ul>
    </div>
  </main>
</body>
</html>
```